Taste of Kerwin digital board & Corflute design

Hi, we are a restaurant based in Parramatta (NSW). We are looking forward for a creative design for our menu to attract the customers at our two different locations.
1. We need a 80 x 296 cm digital board design for display of menu items.
few of the drafts are attached to provide a reference. However, we would request not the similar ones but certain novel and creative designs.
2. We need 3 different 900x1200mm 'A-Frame' or Corflute designs to
-- display our opening hours and details
-- display our flagship items of chaat counter(lassa thali)
--display our menu for TOK, Brindlemarts
--display our menu for TOK, Harrowgate.

```html
<!DOCTYPE html>
<html lang="en">
<head>
<meta charset="utf-8">
<title>Our Menu</title>
<link rel="stylesheet" href="https://fonts.googleapis.com/css2?family=Dancing+Script:wght@700&family=Source+Sans+3:wght@400;500&display=swap">
<style>
  :root {
    --page: #ffffff;
    --veil: rgba(255, 255, 255, 0.62);
    --card: #ffffff;
    --ink: #2a2118;
    --title: #3a2814;
    --accent: #f7941d;
    --food-warm: #d9b27a;
    --food-olive: #7d7a3c;
  }
  * { margin: 0; padding: 0; box-sizing: border-box; }
  html, body {
    width: 1200px;
    height: 462px;
    overflow: hidden;
    background: var(--page);
  }
  .menu-board {
    position: absolute;
    left: 82px;
    top: 82px;
    width: 1035px;
    height: 280px;
    background:
      radial-gradient(circle at 30% 25%, #e98a3a 0 6%, transparent 14%),
      radial-gradient(circle at 88% 40%, #efe2b4 0 14%, transparent 26%),
      radial-gradient(circle at 60% 90%, #b86a2c 0 8%, transparent 18%),
      linear-gradient(90deg, var(--food-olive) 0%, var(--food-warm) 18%, #e8d6b6 50%, var(--food-warm) 80%, #c9a574 100%);
    box-shadow: 10px 10px 14px rgba(0, 0, 0, 0.35);
  }
  .menu-board__veil {
    position: absolute;
    left: 31px;
    top: 14px;
    width: 972px;
    height: 251px;
    background: var(--veil);
  }
  .menu-board__title {
    position: absolute;
    left: 0;
    width: 100%;
    top: 100px;
    text-align: center;
    font-family: "Dancing Script", cursive;
    font-weight: 700;
    font-size: 40px;
    line-height: 1;
    color: var(--title);
  }
  .menu-card {
    position: absolute;
    top: 152px;
    width: 129px;
    height: 175px;
    background: var(--card);
    text-align: center;
    font-family: "Source Sans 3", sans-serif;
    color: var(--ink);
  }
  .menu-card__photo {
    width: 129px;
    height: 129px;
  }
  .menu-card__name {
    margin-top: 3px;
    font-size: 12.6px;
    font-weight: 400;
    color: var(--accent);
    line-height: 15px;
    white-space: nowrap;
  }
  .menu-card__item {
    font-size: 11px;
    line-height: 12.2px;
    white-space: nowrap;
  }
  .menu-card--momos   { left: 161px; }
  .menu-card--thali   { left: 349px; }
  .menu-card--list    { left: 537px; padding-top: 10px; }
  .menu-card--biryani { left: 723px; }
  .menu-card--drinks  { left: 910px; }
  .menu-card--list .menu-card__name { margin-top: 0; margin-bottom: 2px; }
  .menu-card--list .menu-card__item { line-height: 14.5px; }
  .menu-card--list .menu-card__group + .menu-card__group { margin-top: 7px; }
  .menu-card--list .menu-card__group--tight .menu-card__item { line-height: 11.8px; }

  .photo--momos   { background: radial-gradient(circle at 48% 50%, #f2eee8 0 30%, #e69a3c 30% 36%, #f2eee8 36% 44%, #6e6a68 46%, #4a4644 100%); }
  .photo--thali   { background: radial-gradient(circle at 55% 50%, #e2b45c 0 22%, #f4f1ea 24% 48%, #5f5a57 52%, #433f3d 100%); }
  .photo--biryani { background: radial-gradient(circle at 50% 55%, #f3ead6 0 34%, #3a3532 40%, #7a3a24 80%, #5a2a1c 100%); }
  .photo--drinks  { background: radial-gradient(ellipse at 50% 52%, #e9c58c 0 18%, #6a6362 26%, #4c4746 100%); }
</style>
</head>
<body>
  <div class="menu-board" role="img" aria-label="Photo of a spread of Indian dishes: samosas, jalebi, chutneys, rice and curries">
    <div class="menu-board__veil"></div>
  </div>

  <h1 class="menu-board__title">Our Menu</h1>

  <div class="menu-card menu-card--momos">
    <div class="menu-card__photo photo--momos" role="img" aria-label="Photo of steamed momos on a plate with dipping sauce"></div>
    <p class="menu-card__name">MOMOS</p>
    <p class="menu-card__item">VEG MOMOS</p>
    <p class="menu-card__item">CHICKEN MOMOS</p>
  </div>

  <div class="menu-card menu-card--thali">
    <div class="menu-card__photo photo--thali" role="img" aria-label="Photo of a thali tray with paratha, dal and curry"></div>
    <p class="menu-card__name">THALI</p>
    <p class="menu-card__item">VEG THALI</p>
    <p class="menu-card__item">NON-VEG THALI</p>
  </div>

  <div class="menu-card menu-card--list">
    <div class="menu-card__group">
      <p class="menu-card__name">INDIAN STREET FOOD</p>
      <p class="menu-card__item">PANI PURI</p>
      <p class="menu-card__item">CHAAT PAPDI</p>
      <p class="menu-card__item">SAMOSA CHAAT</p>
      <p class="menu-card__item">BHEL PURI</p>
    </div>
    <div class="menu-card__group menu-card__group--tight">
      <p class="menu-card__name">CURRIES</p>
      <p class="menu-card__item">VEG CURRIE</p>
      <p class="menu-card__item">NON-VEG CURRIE</p>
    </div>
    <div class="menu-card__group menu-card__group--tight">
      <p class="menu-card__name">COMBO DEAL</p>
      <p class="menu-card__item">SAMOSA WITH CHAI</p>
    </div>
  </div>

  <div class="menu-card menu-card--biryani">
    <div class="menu-card__photo photo--biryani" role="img" aria-label="Photo of a bowl of biryani garnished with herbs"></div>
    <p class="menu-card__name">BIRYANI</p>
    <p class="menu-card__item">VEG BIRYANI</p>
    <p class="menu-card__item">NON-VEG BIRYANI</p>
  </div>

  <div class="menu-card menu-card--drinks">
    <div class="menu-card__photo photo--drinks" role="img" aria-label="Photo of a mango lassi in a lidded cup"></div>
    <p class="menu-card__name">DRINKS</p>
    <p class="menu-card__item">MANGO LASSI</p>
    <p class="menu-card__item">MASALA CHAI</p>
  </div>
</body>
</html>
```